Business Card Design

Professional solutions in (servers, security, networks, programming)

Industry/Entity Type

Business

Contact Information for Business Card

Tarek Hounayni
Internet services and network solutions
DPV - RTLK - RTLB
netcare@qo-lam.com / 05917406238
www.qo-lam.com

```html
<!DOCTYPE html>
<html lang="en">
<head>
<meta charset="utf-8">
<title>Velmark Co — Business Card</title>
<link rel="stylesheet" href="https://fonts.googleapis.com/css2?family=Teko:wght@500&family=Open+Sans:wght@400;700&display=swap">
<style>
  :root {
    --page-bg: #d9d6d0;
    --card-deep: #0b2f40;
    --card-mid: #174a60;
    --card-glow: #8a9aa2;
    --ink-bright: #f2f4f5;
    --ink-soft: #c9d3d8;
    --ink-muted: #9fb0b8;
    --rule: #e6ecef;
  }
  * { box-sizing: border-box; margin: 0; padding: 0; }
  html, body {
    width: 1200px; height: 1022px; overflow: hidden;
    background: var(--page-bg);
  }
  .stage {
    width: 1200px; height: 1022px;
    display: flex; align-items: center; justify-content: center;
  }
  .card {
    position: relative;
    width: 900px; height: 514px;
    border-radius: 22px;
    overflow: hidden;
    background:
      radial-gradient(ellipse 480px 300px at 52% 42%, var(--card-glow) 0%, rgba(60,90,105,0.55) 40%, rgba(23,74,96,0) 75%),
      linear-gradient(160deg, var(--card-mid) 0%, var(--card-deep) 100%);
    box-shadow: 0 18px 40px rgba(0,0,0,0.25);
    font-family: "Open Sans", Arial, sans-serif;
    color: var(--ink-bright);
  }
  .divider {
    position: absolute; left: 0; right: 0; top: 292px;
    height: 2px; background: var(--rule);
  }
  .brand {
    position: absolute; left: 50px; top: 44px;
  }
  .brand-name {
    font-family: "Teko", "Arial Narrow", sans-serif;
    font-weight: 500;
    font-size: 108px; line-height: 0.9;
    letter-spacing: 2px;
    color: var(--ink-bright);
  }
  .brand-tagline {
    font-size: 25px; color: var(--ink-muted);
    margin-top: 4px; letter-spacing: 0.5px;
  }
  .brand-tagline-spaced {
    font-size: 18px; color: var(--ink-muted);
    letter-spacing: 17px; margin-top: 2px;
  }
  .person {
    position: absolute; right: 44px; top: 246px; text-align: right;
  }
  .person-name {
    font-weight: 700; font-size: 30px; letter-spacing: 1px;
    text-transform: uppercase;
  }
  .person-credentials {
    position: absolute; right: 44px; top: 304px;
    font-size: 17px; color: var(--ink-soft); letter-spacing: 1px;
  }
  .contacts {
    position: absolute; left: 150px; top: 330px;
    list-style: none;
  }
  .contacts li {
    display: flex; align-items: center; gap: 12px;
    font-size: 22px; line-height: 34px; color: var(--ink-bright);
  }
  .contacts svg { width: 16px; height: 16px; flex: none; }
</style>
</head>
<body>
  <main class="stage">
    <article class="card">
      <div class="brand">
        <div class="brand-name">VELMARK CO</div>
        <div class="brand-tagline">Internet services and network</div>
        <div class="brand-tagline-spaced">solutions</div>
      </div>

      <div class="person">
        <div class="person-name">Tarek Hounayni</div>
      </div>
      <div class="divider"></div>
      <div class="person-credentials">DPV - RTLK - RTLB</div>

      <ul class="contacts">
        <li>
          <svg viewBox="0 0 16 16" aria-hidden="true"><path d="M4 1.5l2.2 2.8-1.3 1.7c.9 2 2.3 3.5 4.3 4.4l1.7-1.3 2.8 2.2-1.3 2.4C7.4 13.5 2.5 8.6 1.6 3z" fill="var(--ink-soft)"/></svg>
          05917406238
        </li>
        <li>
          <svg viewBox="0 0 16 16" aria-hidden="true"><rect x="1.5" y="3.5" width="13" height="9" fill="none" stroke="var(--ink-soft)" stroke-width="1.5"/><path d="M1.5 3.5L8 9l6.5-5.5" fill="none" stroke="var(--ink-soft)" stroke-width="1.5"/></svg>
          netcare@qo-lam.com
        </li>
        <li>
          <svg viewBox="0 0 16 16" aria-hidden="true"><g fill="none" stroke="var(--ink-soft)" stroke-width="1.3"><circle cx="8" cy="8" r="6.3"/><ellipse cx="8" cy="8" rx="2.7" ry="6.3"/><path d="M1.7 8h12.6M2.8 4.8h10.4M2.8 11.2h10.4"/></g></svg>
          www.qo-lam.com
        </li>
      </ul>
    </article>
  </main>
</body>
</html>
```